Company raising consciousness thru leadership & self-awareness needs amazing Letterhead

We are a technology company that spun out of a consulting firm. We are waking people up in corporate America through surveys, leadership development, workshops and consulting. Getting employees to become self-aware and changing company culture through improved leadership and team effectiveness. We need Word letterhead for our proposals, handouts, and worksheets that match our brand standard, is fresh, and communicates trust, credibility and professionalism.

Target Market(s)

Our target clients are other businesses, and executive leaders and C-suite leaders in those companies.

Font styles to use
Sans Serif

Requirements
Must have
• A Word template we can use for handouts, proposals, executive summary, project management documents, and letters. We need our logo. Please add page number and date on the footer. Must match the theme of our new website in look and feel to match the brand we are trying to promote. Use the colors from our brand standard document I submitted.

```html
<!DOCTYPE html>
<html lang="en">
<head>
<meta charset="utf-8">
<title>Veralume Letterhead</title>
<link href="https://fonts.googleapis.com/css2?family=Lato:wght@400;700&display=swap" rel="stylesheet">
<style>
  :root {
    --navy: #244a93;
    --sky: #2fbde8;
    --paper: #ffffff;
    --ink: #3d3d3d;
    --backdrop: #d6cfcc;
  }
  html, body {
    margin: 0;
    width: 1200px;
    height: 784px;
    overflow: hidden;
    background: var(--backdrop);
    font-family: "Lato", sans-serif;
  }
  .letterhead {
    position: absolute;
    left: 357px;
    top: 22px;
    width: 486px;
    height: 740px;
    background: var(--paper);
    box-shadow: 0 2px 10px rgba(0,0,0,0.12);
  }
  .side-band {
    position: absolute;
    left: 0;
    width: 22px;
  }
  .side-band--accent { top: 0; height: 160px; background: var(--sky); }
  .side-band--main { top: 165px; bottom: 0; background: var(--navy); }

  .brand {
    position: absolute;
    left: 44px;
    top: 46px;
    display: flex;
    align-items: center;
    gap: 10px;
  }
  .brand__mark {
    width: 30px;
    height: 30px;
    border-radius: 50%;
    background: var(--navy);
  }
  .brand__name {
    font-weight: 700;
    font-size: 26px;
    letter-spacing: 1.5px;
    color: var(--navy);
  }
  .brand__tagline {
    position: absolute;
    left: 84px;
    top: 82px;
    font-size: 9px;
    letter-spacing: 1.6px;
    color: var(--navy);
  }

  .contact {
    position: absolute;
    left: 22px;
    bottom: 34px;
    display: flex;
  }
  .contact__icons {
    width: 22px;
    background: var(--navy);
    padding: 8px 0;
    display: flex;
    flex-direction: column;
    align-items: center;
    gap: 7px;
    border: 2px solid var(--paper);
    border-left: none;
  }
  .contact__icons svg { width: 11px; height: 11px; display: block; }
  .contact__icons .icon--pin { margin-bottom: 9px; }
  .contact__details {
    padding: 6px 0 0 8px;
    font-size: 10.5px;
    line-height: 15px;
    color: var(--ink);
  }
  .contact__details p { margin: 0; }
</style>
</head>
<body>
  <main class="letterhead">
    <div class="side-band side-band--accent"></div>
    <div class="side-band side-band--main"></div>

    <header class="brand">
      <span class="brand__mark"></span>
      <span class="brand__name">VERALUME</span>
    </header>
    <div class="brand__tagline">MINDFUL LEADERSHIP</div>

    <footer class="contact">
      <div class="contact__icons">
        <svg class="icon--pin" viewBox="0 0 12 12" aria-label="Address"><path d="M6 1a3.5 3.5 0 0 0-3.5 3.5C2.5 7 6 11 6 11s3.5-4 3.5-6.5A3.5 3.5 0 0 0 6 1z" fill="#fff"/><circle cx="6" cy="4.5" r="1.3" fill="#244a93"/></svg>
        <svg viewBox="0 0 12 12" aria-label="Phone"><path d="M3 1.5l1.8 2.2-1 1.2c.6 1.3 1.6 2.3 2.9 2.9l1.2-1 2.2 1.8-1 1.9C5.5 10.3 1.7 6.5 1.5 2.5z" fill="#fff"/></svg>
        <svg viewBox="0 0 12 12" aria-label="Email"><rect x="1.5" y="3" width="9" height="6.5" fill="#fff"/><path d="M1.5 3l4.5 3.5L10.5 3" stroke="#244a93" stroke-width="1" fill="none"/></svg>
        <svg viewBox="0 0 12 12" aria-label="Website"><circle cx="6" cy="6" r="4.5" fill="none" stroke="#fff" stroke-width="1"/><ellipse cx="6" cy="6" rx="2" ry="4.5" fill="none" stroke="#fff" stroke-width="0.8"/><path d="M1.5 6h9" stroke="#fff" stroke-width="0.8"/></svg>
      </div>
      <div class="contact__details">
        <p>1234 First Line Address</p>
        <p>5678 Second Line Address</p>
        <p>(111) 999-0000</p>
        <p>Info@yourmail.com</p>
        <p>www.yourwebsite.com</p>
      </div>
    </footer>
  </main>
</body>
</html>
```